One slide graphic for website

I am designing a series of sliders for my website http://new.kelmarbyte.com

The slide I am trying to create has the following message:

EVERY company is a media company.
Empower yours now!

Learn More >

The ideas I have had for imagery are an office building with the letters 'Every Company is a Media Company' either shone onto the building or letters on the building roof ledge ect.

Aby ideas you may have to improve on this would be appreciated.

The idea behind the slide is to promote a software application which gives marketing professionals the chance to increase their media coverage. The message also encourages companies to create their own news on a number of platforms as the media landscape has changed so much. Look at the blue finch stunt whereby they generated 10 million views on viddlo using PR alone.

Good luck and I look forward to seeing your ideas.

Marcus

```html
<!DOCTYPE html>
<html lang="en">
<head>
<meta charset="utf-8">
<title>Kelmarbyte – Every Company Is a Media Company</title>
<link rel="stylesheet" href="https://fonts.googleapis.com/css2?family=Archivo+Black&family=Marcellus+SC&display=swap">
<style>
  :root {
    --sky-top: #e4ecf3;
    --sky-mid: #c9d7e2;
    --horizon: #a9bccb;
    --water: #8ea3b3;
    --city-mid: #6f7d89;
    --city-dark: #3f4852;
    --ink: #0b0b0b;
    --paper: #ffffff;
    --panel-top: #f1ece6;
    --panel-red: #c9322f;
    --panel-green: #9ccc3a;
    --panel-orange: #e0622a;
  }
  * { margin: 0; padding: 0; box-sizing: border-box; }
  html, body { width: 1200px; height: 387px; overflow: hidden; background: var(--paper); }
  .slide {
    position: relative;
    width: 1200px;
    height: 387px;
    overflow: hidden;
  }
  .skyline-photo {
    position: absolute;
    inset: 0;
    background: linear-gradient(180deg,
      var(--sky-top) 0%,
      var(--sky-mid) 34%,
      var(--horizon) 50%,
      var(--water) 58%,
      var(--city-mid) 72%,
      var(--city-dark) 100%);
  }
  .headline {
    position: absolute;
    left: 14px;
    top: 14px;
    width: 470px;
    text-align: center;
    font-family: "Archivo Black", "Arial Black", sans-serif;
    color: var(--ink);
    text-transform: uppercase;
    line-height: 1.0;
    text-shadow:
      -3px -3px 0 var(--paper), 3px -3px 0 var(--paper),
      -3px 3px 0 var(--paper), 3px 3px 0 var(--paper),
      0 -3px 0 var(--paper), 0 3px 0 var(--paper),
      -3px 0 0 var(--paper), 3px 0 0 var(--paper),
      0 0 10px var(--paper);
  }
  .headline .lead { display: block; font-size: 64px; letter-spacing: 1px; }
  .headline .rest { display: block; font-size: 45px; letter-spacing: -0.3px; margin-top: 4px; }
  .tagline {
    position: absolute;
    left: 616px;
    top: 46px;
    font-family: "Marcellus SC", serif;
    color: var(--ink);
    font-size: 56px;
    line-height: 1.0;
    white-space: nowrap;
    text-shadow: 0 0 8px var(--paper), 0 0 3px var(--paper);
  }
  .tagline span { display: block; }
  .tagline .second { margin-left: 12px; margin-top: 0; word-spacing: 6px; font-size: 52px; }
  .showcase {
    position: absolute;
    left: 942px;
    top: 0;
    width: 258px;
    height: 387px;
    background: linear-gradient(160deg,
      var(--panel-top) 0%,
      var(--panel-red) 22%,
      var(--panel-green) 34%,
      var(--panel-top) 48%,
      var(--panel-orange) 72%,
      var(--panel-top) 100%);
  }
  .learn-more {
    position: absolute;
    left: 948px;
    top: 145px;
    width: 252px;
    height: 101px;
    padding-left: 26px;
    background: var(--paper);
    display: flex;
    align-items: center;
    justify-content: flex-start;
    white-space: nowrap;
    font-family: "Marcellus SC", serif;
    font-size: 35px;
    color: var(--ink);
    text-decoration: none;
    box-shadow: 0 0 6px rgba(0,0,0,0.25);
  }
</style>
</head>
<body>
  <main class="slide">
    <div class="skyline-photo" role="img" aria-label="Aerial view of a city skyline with a tall spire skyscraper and a river under a pale blue sky"></div>

    <h1 class="headline">
      <span class="lead">Every</span>
      <span class="rest">Company is a</span>
      <span class="rest">Media Company.</span>
    </h1>

    <p class="tagline">
      <span>Empower</span>
      <span class="second">yours now!</span>
    </p>

    <div class="showcase" role="img" aria-label="Collage of website and app screenshots"></div>

    <a class="learn-more" href="http://new.kelmarbyte.com">Learn More &gt;</a>
  </main>
</body>
</html>
```